Business Card Design

redesign of card and recreation of logo based on image provided. the business is located in new york so the Brooklyn Bridge figures prominently in the scheme. product should be very clean.

Industry/Entity Type

Real Estate

Contact Information for Business Card

Wendell Ortwick 318 Tamsin Street Brooklyn, New York 11409 wendell@qorvane.com Mobile: 917-555-0143

Colors
cadf82
1b1b1b
ffffff

Requirements
Nice to have
• Brooklyn Bridge

```html
<!DOCTYPE html>
<html lang="en">
<head>
<meta charset="utf-8">
<title>Ortwick &amp; Assoc. — Business Card</title>
<link href="https://fonts.googleapis.com/css2?family=Questrial&display=swap" rel="stylesheet">
<style>
  :root {
    --lime: #cadf82;
    --ink: #1b1b1b;
    --paper: #ffffff;
    --card-dark: #2b2b2b;
    --stage: #e9e7e3;
    --muted: #555555;
  }
  * { box-sizing: border-box; margin: 0; padding: 0; }
  html, body {
    width: 1200px; height: 900px; overflow: hidden;
    background: var(--stage);
    font-family: "Questrial", "Century Gothic", sans-serif;
  }
  .canvas { position: relative; width: 1200px; height: 900px; }

  .card {
    position: absolute;
    width: 560px; height: 320px;
    border-radius: 18px;
    box-shadow: 0 10px 28px rgba(0,0,0,0.18);
  }

  /* Back of card */
  .card-back {
    left: 110px; top: 90px;
    background: var(--card-dark);
    display: flex; flex-direction: column;
    align-items: center; justify-content: center;
    color: var(--paper);
  }
  .card-back .brand-name { color: var(--paper); }
  .card-back .brand-place { color: var(--lime); }
  .card-back .website {
    margin-top: 34px;
    color: var(--lime);
    font-size: 17px; letter-spacing: 1px;
  }

  /* Brand lockup */
  .brand { display: flex; flex-direction: column; align-items: flex-end; }
  .brand-row { display: flex; align-items: center; gap: 12px; }
  .brand-dot { width: 22px; height: 22px; border-radius: 50%; background: var(--lime); }
  .brand-name { font-size: 34px; letter-spacing: 0.5px; color: var(--ink); }
  .brand-place { font-size: 14px; letter-spacing: 4px; margin-top: 2px; color: var(--ink); }

  /* Front of card */
  .card-front {
    left: 530px; top: 480px;
    background: var(--paper);
    display: flex; align-items: center;
    padding: 0 34px 0 30px;
  }
  .card-front .brand { width: 270px; }
  .card-front .brand-name { font-size: 27px; }
  .card-front .brand-place { font-size: 12px; color: #3a3a3a; }

  .contact { margin-left: 24px; color: var(--ink); }
  .contact-name { font-size: 27px; line-height: 1.1; }
  .contact-role {
    color: var(--lime); font-size: 15px; letter-spacing: 3px;
    margin: 2px 0 10px;
  }
  .contact-list { list-style: none; font-size: 17px; line-height: 1.45; }
  .contact-list li { display: flex; align-items: center; gap: 10px; }
  .contact-list .icon { width: 16px; height: 16px; flex: none; fill: var(--lime); }
  .contact-list .indent { padding-left: 26px; }
</style>
</head>
<body>
<main class="canvas">

  <section class="card card-back" aria-label="Card back">
    <div class="brand">
      <div class="brand-row">
        <span class="brand-dot"></span>
        <span class="brand-name">Ortwick &amp; Assoc.</span>
      </div>
      <span class="brand-place">NEW YORK</span>
    </div>
    <p class="website">www.qorvane.com</p>
  </section>

  <section class="card card-front" aria-label="Card front">
    <div class="brand">
      <div class="brand-row">
        <span class="brand-dot"></span>
        <span class="brand-name">Ortwick &amp; Assoc.</span>
      </div>
      <span class="brand-place">NEW YORK</span>
    </div>

    <div class="contact">
      <h1 class="contact-name">Wendell Ortwick</h1>
      <p class="contact-role">BROKER</p>
      <ul class="contact-list">
        <li>
          <svg class="icon" viewBox="0 0 16 16" aria-hidden="true"><path d="M1 5c0-2 3-3 7-3s7 1 7 3v1h-3V5H4v1H1zM3 7h10l1 7H2z"/></svg>
          718 555 0192
        </li>
        <li>
          <svg class="icon" viewBox="0 0 16 16" aria-hidden="true"><path d="M4 0h8a1 1 0 0 1 1 1v14a1 1 0 0 1-1 1H4a1 1 0 0 1-1-1V1a1 1 0 0 1 1-1zm1 2v10h6V2zm3 11a1 1 0 1 0 0 2 1 1 0 0 0 0-2z"/></svg>
          917 555 0143
        </li>
        <li>
          <svg class="icon" viewBox="0 0 16 16" aria-hidden="true"><path d="M0 3h16v1L8 9 0 4zm0 3 8 5 8-5v7H0z"/></svg>
          wendell@qorvane.com
        </li>
        <li>
          <svg class="icon" viewBox="0 0 16 16" aria-hidden="true"><path d="M8 0a5.5 5.5 0 0 1 5.5 5.5C13.5 10 8 16 8 16S2.5 10 2.5 5.5A5.5 5.5 0 0 1 8 0zm0 3a2.5 2.5 0 1 0 0 5 2.5 2.5 0 0 0 0-5z"/></svg>
          318 Tamsin Street
        </li>
        <li class="indent">Brooklyn, NY 11409</li>
      </ul>
    </div>
  </section>

</main>
</body>
</html>
```